Der Designer hat mir ein super Logo entworfen sehr schnell tolle Zusammenarbeit. Ist nur zu empfehlen
Zielgruppe
Es handelt sich um eine Haus und Immobilienverwaltung die Zielgruppe sind Eigentümer der Häuser und Firmen
Aufgabenstellung
Edel klassisch

```html
<!DOCTYPE html>
<html lang="de">
<head>
<meta charset="utf-8">
<title>Harlenbeck Unternehmensgruppe – Geschäftsausstattung</title>
<link href="https://fonts.googleapis.com/css2?family=Questrial&display=swap" rel="stylesheet">
<style>
  :root {
    --stage: #4b4b4b;
    --card-dark: #353535;
    --card-light: #ffffff;
    --blue: #78afc9;
    --green: #83a897;
    --grey-text: #5f5f5f;
    --grey-name: #7d8078;
    --grey-logo: #b3b3b3;
    --grey-band: #b5b5b5;
    --divider: #d6d6d6;
    --faint: #edf2f6;
  }
  * { margin: 0; padding: 0; box-sizing: border-box; }
  html, body { width: 1200px; height: 1200px; overflow: hidden; }
  body { background: var(--stage); font-family: "Questrial", sans-serif; position: relative; }

  .card { position: absolute; width: 467px; height: 302px; overflow: hidden; }
  .card--front { left: 366px; top: 257px; background: var(--card-dark); }
  .card--back { top: 644px; background: var(--card-light); }
  .card--back-a { left: 76px; }
  .card--back-b { left: 656px; }

  /* front wordmark */
  .front-brand { position: absolute; left: 0; right: 0; top: 112px; text-align: center; }
  .front-brand__name { display: inline-flex; align-items: center; gap: 12px; color: var(--blue); font-size: 40px; letter-spacing: 4px; }
  .front-brand__square { width: 22px; height: 22px; background: var(--green); }
  .front-brand__sub { margin-top: 10px; color: var(--grey-logo); font-size: 13.5px; letter-spacing: 2.4px; }

  /* back side */
  .watermark { position: absolute; left: 10px; top: 125px; font-size: 96px; color: var(--faint); letter-spacing: -2px; white-space: nowrap; }
  .divider { position: absolute; left: 192px; top: 22px; width: 1px; height: 226px; background: var(--divider); }
  .back-brand { position: absolute; right: 27px; top: 50px; text-align: right; }
  .back-brand__name { display: inline-flex; align-items: center; gap: 7px; color: var(--blue); font-size: 24px; letter-spacing: 2px; }
  .back-brand__square { width: 12px; height: 12px; background: var(--green); }
  .back-brand__sub { margin-top: 6px; color: var(--grey-logo); font-size: 7.4px; letter-spacing: 1.3px; }

  .person { position: absolute; left: 0; width: 183px; top: 112px; text-align: center; }
  .person__name { color: var(--grey-name); font-size: 21px; }
  .person__role { color: var(--grey-text); font-size: 11px; margin-top: 2px; }

  .contact { position: absolute; right: 27px; top: 146px; width: 210px; font-size: 12.5px; color: var(--grey-text); }
  .contact__address { text-align: right; white-space: nowrap; }
  .contact__heading { text-align: right; color: var(--green); margin-top: 11px; font-size: 13px; }
  .contact__row { display: flex; justify-content: space-between; margin-top: 6px; white-space: nowrap; }
  .contact__label { color: var(--blue); }

  .band { position: absolute; left: 0; right: 0; top: 263px; height: 11px; }
  .band__grey { position: absolute; left: 0; width: 79px; height: 100%; background: var(--grey-band); }
  .band__green { position: absolute; left: 138px; right: 0; height: 100%; background: var(--green); }
  .band__square { position: absolute; left: 94px; top: 249px; width: 26px; height: 26px; background: var(--blue); }
</style>
</head>
<body>

<section class="card card--front">
  <div class="front-brand">
    <div class="front-brand__name"><span class="front-brand__square"></span>HARLENBECK</div>
    <div class="front-brand__sub">UNTERNEHMENSGRUPPE GmbH</div>
  </div>
</section>

<section class="card card--back card--back-a">
  <div class="watermark" aria-hidden="true">Harlenbeck</div>
  <div class="divider"></div>
  <div class="back-brand">
    <div class="back-brand__name"><span class="back-brand__square"></span>HARLENBECK</div>
    <div class="back-brand__sub">UNTERNEHMENSGRUPPE GmbH</div>
  </div>
  <div class="person">
    <div class="person__name">Lena Harlenbeck</div>
    <div class="person__role">Geschäftsführer</div>
  </div>
  <div class="contact">
    <div class="contact__address">Lindenauer Weg 12 | 10115 Berlin</div>
    <div class="contact__heading">Kontakt</div>
    <div class="contact__row"><span class="contact__label">Telefon:</span><span>+49 030 555 02 148</span></div>
    <div class="contact__row"><span class="contact__label">Telefax:</span><span>+49 030 555 02 148</span></div>
    <div class="contact__row"><span class="contact__label">E-Mail:</span><span>kontakt@harlenbeck-gmbh.de</span></div>
  </div>
  <div class="band"><span class="band__grey"></span><span class="band__green"></span></div>
  <div class="band__square"></div>
</section>

<section class="card card--back card--back-b">
  <div class="divider"></div>
  <div class="back-brand">
    <div class="back-brand__name"><span class="back-brand__square"></span>HARLENBECK</div>
    <div class="back-brand__sub">UNTERNEHMENSGRUPPE GmbH</div>
  </div>
  <div class="person">
    <div class="person__name">Lena Harlenbeck</div>
    <div class="person__role">Geschäftsführer</div>
  </div>
  <div class="contact">
    <div class="contact__address">Lindenauer Weg 12 | 10115 Berlin</div>
    <div class="contact__heading">Kontakt</div>
    <div class="contact__row"><span class="contact__label">Telefon:</span><span>+49 030 555 02 148</span></div>
    <div class="contact__row"><span class="contact__label">Telefax:</span><span>+49 030 555 02 148</span></div>
    <div class="contact__row"><span class="contact__label">E-Mail:</span><span>kontakt@harlenbeck-gmbh.de</span></div>
  </div>
  <div class="band"><span class="band__grey"></span><span class="band__green"></span></div>
  <div class="band__square"></div>
</section>

</body>
</html>
```